Flyer-Design für Immobilienbüro
Zielgruppe
Wir sind ein Immobilienbüro. Es sollen Immobilienverkäufer angesprochen werden um uns zu beauftragen Ihre Immobilie zu verkaufen. Motto sollte sein: ' Immobilienverkauf ist stressig. JA. Aber nicht für Sie '.
Aufgabenstellung
DIN A5 hochkant. beidseitig bedruckt. auf Rückseite unten soll Antwortkarte an uns adressiert sein sein.
Es sollen Immobilienverkäufer angesprochen werden um uns zu beauftragen Ihre Immobilie zu verkaufen. Motto sollte sein: ' Immobilienverkauf ist stressig. JA. Aber nicht für Sie '.
(Dies sollte auch durch ein Bild dargestellt werden)
Rundum-Sorglos Immobilienverkauf - 100% kostenlos für Sie als Eigentümer
es sollte auf dem Flyer vermerkt sein:
- Unser Service ist für Sie als Verkäufer 100 % KOSTENLOS
- bei einer Beauftragung erhalten Sie den Energieausweis von uns KOSTENLOS
- wir besorgen alle zum Verkauf benötigter Dokumente für Sie KOSTENLOS
- wir sind ständig auf der Suche nach Objekten die wir selbst ankaufen. Kaufentscheidung innerhalb von 2 Tagen.
- FÜR TIPPGEBER: Sie kennen jemanden, der eine Immobilie zu verkaufen hat? Tippgeber erhalten bis zu 5.000,- Euro Provision in Bar. Kontraktieren Sie uns.
Design soll hochwertig und elegant sein.
Als Kontakttelefonnummer soll diese vermerkt sein.
Antwortkarte auf der Rückseite sollte Antworttext in etwa enthalten:
O Wir haben eine Immobile zu verkaufen. Rufen Sie uns bitte an
O Wir haben demnächst eine Immobilien zu verkaufen. Rufen Sie uns bitte an.
O Ich kenne jemanden der seine Immobilie verkauft und möchte Tipgeber sein
Name / Vorname
Straße / PLZ / Ort
Telefonnummer

```html
<!DOCTYPE html>
<html lang="de">
<head>
<meta charset="utf-8">
<title>Flyer Immobilienverkauf – Vorder- und Rückseite</title>
<link href="https://fonts.googleapis.com/css2?family=Crimson+Pro:wght@400;600;700&display=swap" rel="stylesheet">
<style>
  :root {
    --green: #4f7f37;
    --tan: #a89d72;
    --ink: #1f1f1f;
    --dark: #232323;
    --paper: #ffffff;
    --stage: #e8e5e0;
    --rule: #555555;
  }
  * { margin: 0; padding: 0; box-sizing: border-box; }
  html, body { width: 1200px; height: 800px; overflow: hidden; }
  body {
    background: var(--stage);
    font-family: "Crimson Pro", Georgia, serif;
    color: var(--ink);
    position: relative;
  }
  .page {
    position: absolute;
    top: 21px;
    width: 540px;
    height: 758px;
    background: var(--paper);
    overflow: hidden;
    box-shadow: 0 2px 8px rgba(0,0,0,.18);
  }
  .page--front { left: 40px; }
  .page--back { left: 620px; }
  .abs { position: absolute; }

  /* Front */
  .headline {
    top: 0; left: 0; width: 540px; height: 59px;
    display: flex; align-items: center; justify-content: center;
    font-weight: 700; font-size: 22px;
  }
  .offer-band {
    top: 59px; left: 0; width: 540px; height: 72px;
    background: var(--green); color: #fff;
    text-align: center; font-weight: 700; font-size: 20.5px; line-height: 1.3;
    padding-top: 8px;
  }
  .owners-photo {
    top: 143px; left: 0; width: 283px; height: 222px;
    background: linear-gradient(90deg, #8a9a86 0%, #c9cfd3 45%, #e8ebee 85%, #fff 100%);
  }
  .services {
    top: 155px; left: 279px; width: 222px;
    font-size: 12.6px; line-height: 1.32; text-align: justify;
  }
  .services p { margin-bottom: 15px; }
  .services b { font-weight: 700; }
  .relax-band {
    top: 374px; left: 0; width: 540px; height: 77px;
    background: var(--tan); color: #fff;
    font-weight: 700; font-size: 12.4px; line-height: 1.35;
    padding: 23px 0 0 48px;
  }
  .team-photo {
    top: 451px; left: 0; width: 540px; height: 234px;
    background: linear-gradient(180deg, #b9b9b9 0%, #d6d6d6 55%, #7b7b7b 100%);
  }
  .cta-shape { top: 0; left: 0; }
  .cta-text {
    top: 656px; left: 281px; color: #fff;
    font-size: 19px; line-height: 1.3;
    transform: rotate(-7.5deg); transform-origin: left top;
    white-space: nowrap;
  }
  .brand {
    top: 708px; left: 50px;
    display: flex; align-items: center; gap: 8px;
    font-size: 17px; font-weight: 600; color: var(--green);
  }
  .brand__dot {
    width: 10px; height: 10px; border-radius: 50%; background: var(--green);
  }

  /* Back */
  .back-art { top: 0; left: 0; }
  .rotated {
    transform-origin: left top; white-space: nowrap; line-height: 1.25;
  }
  .note { top: 92px; left: 55px; transform: rotate(-8deg); font-size: 13.4px; color: var(--ink); }
  .tip { top: 199px; left: 140px; transform: rotate(-7deg); font-size: 13.4px; color: #fff; }
  .rotated h3 { font-size: 13.4px; font-weight: 700; letter-spacing: .3px; }
  .privacy {
    top: 349px; left: 49px; font-size: 7.6px; line-height: 1.3;
  }
  .cut-line {
    top: 373px; left: 0; width: 540px;
    border-top: 1px dashed #777;
  }
  .scissors { top: 364px; left: 26px; font-size: 11px; color: #555; background: #fff; }
  .reply-options { top: 398px; left: 26px; width: 230px; list-style: none; }
  .reply-options li {
    position: relative; padding-left: 22px;
    font-size: 11.6px; line-height: 1.3; margin-bottom: 15px;
  }
  .reply-options li::before {
    content: ""; position: absolute; left: 0; top: 1px;
    width: 13px; height: 13px; border: 1px solid #333; border-radius: 50%;
  }
  .field {
    left: 33px; width: 218px; border-top: 1px solid var(--rule);
    font-size: 8.6px; padding-top: 5px;
  }
  .divider { top: 400px; left: 272px; width: 1px; height: 321px; background: #333; }
  .stamp {
    top: 393px; left: 413px; width: 71px; height: 95px;
    border: 1px solid #444;
    display: flex; align-items: center; justify-content: center;
    text-align: center; font-size: 11.2px; line-height: 1.35;
  }
  .address { top: 592px; left: 289px; font-size: 13.8px; line-height: 1.35; }
  .address p + p { margin-top: 11px; }
</style>
</head>
<body>

<section class="page page--front">
  <h1 class="abs headline">Immobilienverkauf ist stressig. JA. Aber nicht für Sie!</h1>
  <h2 class="abs offer-band">Rundum-Sorglos Immobilienverkauf -<br>100% kostenlos für Sie als Eigentümer</h2>
  <div class="abs owners-photo" role="img" aria-label="Foto: entspanntes älteres Ehepaar vor seinem hellen Haus"></div>
  <div class="abs services">
    <p>Unser Service ist für Sie als Verkäufer <b>kostenlos:</b> wir machen die Fotos, erstellen ein Exposé und führen Besichtigungen sowie Verhandlungen mit Interessenten durch - bis zum Notartermin</p>
    <p>Der vorgeschriebene Energieausweis wird <b>ohne Aufpreis</b> von uns für Sie erstellt</p>
    <p>Wir besorgen alle zum Verkauf benötigten Dokumente <b>ohne Mehrkosten</b></p>
  </div>
  <div class="abs relax-band">Lehnen Sie sich entspannt zurück - wir kümmern uns um alles.<br>Nur unterschreiben müssen Sie selbst.</div>
  <div class="abs team-photo" role="img" aria-label="Schwarz-Weiß-Foto: die drei Makler des Büros in Anzügen"></div>
  <svg class="abs cta-shape" width="540" height="758" aria-hidden="true">
    <polygon points="266,654 540,618 540,692 276,726" fill="var(--green)"/>
  </svg>
  <div class="abs cta-text">Informieren Sie sich direkt<br>unter 08231 44718-20</div>
  <div class="abs brand">
    <span class="brand__dot"></span>
    <span>Berger Lenz Immobilien</span>
  </div>
</section>

<section class="page page--back">
  <svg class="abs back-art" width="540" height="380">
    <defs>
      <linearGradient id="fade" x1="0" y1="0" x2="0" y2="1">
        <stop offset="0" stop-color="#8e8e8e"/>
        <stop offset="1" stop-color="#ffffff"/>
      </linearGradient>
      <linearGradient id="wood" x1="0" y1="0" x2="1" y2="1">
        <stop offset="0" stop-color="#9c968c"/>
        <stop offset="1" stop-color="#d9d4cb"/>
      </linearGradient>
      <linearGradient id="hands" x1="0" y1="0" x2="1" y2="1">
        <stop offset="0" stop-color="#6e4a33"/>
        <stop offset="0.5" stop-color="#c98f6a"/>
        <stop offset="1" stop-color="#7a5238"/>
      </linearGradient>
    </defs>
    <polygon points="0,0 540,0 540,160 0,200" fill="var(--dark)"/>
    <polygon points="0,130 540,90 540,300 0,300" fill="url(#fade)"/>
    <polygon points="313,10 540,0 540,135 330,152" fill="url(#wood)" role="img" aria-label="Foto: Hausschlüssel mit Hausanhänger auf Holz"/>
    <polygon points="0,74 353,31 363,128 0,177" fill="var(--tan)"/>
    <polygon points="118,177 540,124 540,235 130,284" fill="var(--dark)"/>
    <polygon points="313,239 498,218 511,342 329,363" fill="url(#hands)" role="img" aria-label="Foto: Hände halten ein Geschenk aus Geldscheinen"/>
  </svg>
  <div class="abs rotated note">
    <h3>ÜBRIGENS:</h3>
    Wir sind ständig auf der Suche nach Objekten die<br>wir selbst ankaufen. Kaufentscheidung innerhalb<br>von 2 Tagen.
  </div>
  <div class="abs rotated tip">
    <h3>FÜR TIPPGEBER:</h3>
    Sie kennen jemanden, der eine Immobilie zu verkaufen hat?<br>Tippgeber erhalten bis zu 5.000,- Euro Provision in Bar.<br>Kontraktieren Sie uns.
  </div>
  <p class="abs privacy">Informationen zur Verarbeitung Ihrer persönlichen Daten finden Sie unter<br>https://www.berger-lenz.de/impressum/datenschutz</p>
  <div class="abs cut-line"></div>
  <span class="abs scissors">✂</span>
  <ul class="abs reply-options">
    <li>Wir haben eine Immobile zu verkaufen.<br>Rufen Sie uns bitte an</li>
    <li>Wir haben demnächst eine Immobilien zu verkaufen. Rufen Sie uns bitte an.</li>
    <li>Ich kenne jemanden der seine Immobilie verkauft und möchte Tippgeber sein.</li>
  </ul>
  <div class="abs field" style="top:548px">Name / Vorname</div>
  <div class="abs field" style="top:597px">Straße / Nr.</div>
  <div class="abs field" style="top:647px">PLZ / Ort</div>
  <div class="abs field" style="top:692px">Telefonnummer</div>
  <div class="abs divider"></div>
  <div class="abs stamp">Bitte<br>ausreichend<br>frankieren</div>
  <div class="abs address">
    <p>Immobilien Berger und Lenz GbR</p>
    <p>Lindenallee 7<br>86999 Lindenfeld</p>
  </div>
</section>

</body>
</html>
```